Website for legal services (estates law) called TKV ESTATES LAW

Simple, catchy and easy to use. I am providing estates legal services and I want clients to feel a warm, friendly but professional vibe when they visit my website. I don't want harsh legal pictures (like a picture of a tough lawyer, or pictures of scales of justice). Pictures of books, plants, signing documents or a comfortable looking office are acceptable.

Please use wordpress to design it because I want ability to upload blogs on my own through wordpress after. I am attaching my logo.

Target Market(s)

Millenials, boomers, people in their 40's and anyone looking to transfer property titles or create a will, or anyone whose relatives have died and need help with estates administration.

Industry/Entity Type

Law Firm

Coding

Coded - Design and coding required

Number of Pages Required

4 page

Font styles to use
Sans Serif

Colors
0493ce
33a6d7
85cae6
cee9f5
f4fafd

Requirements
Must have
• - Must be designed with WordPress
- Must have a warm, friendly, professional vibe
- I want to be able to edit any of the content of the website myself
Nice to have
• Pictures of law books, plants, signing documents or a comfortable looking office are acceptable.
Should not have
• I don't want harsh legal pictures (like a picture of a tough lawyer, or pictures of scales of justice).

```html
<!DOCTYPE html>
<html lang="en">
<head>
<meta charset="utf-8">
<title>TKV Estates Law</title>
<link href="https://fonts.googleapis.com/css2?family=Mulish:wght@400;500;600;700&display=swap" rel="stylesheet">
<style>
:root{
  --navy:#0b2558;
  --blue:#0d4a9a;
  --teal:#19a37f;
  --text:#5a5a5a;
  --soft:#edf0f5;
  --footer:#06122b;
  --grad:linear-gradient(90deg,var(--blue),var(--teal));
}
*{box-sizing:border-box;margin:0;padding:0}
html,body{width:1200px;height:2914px;overflow:hidden}
body{font-family:'Mulish',sans-serif;color:var(--text);background:#fff;position:relative}
.abs{position:absolute}
/* header */
.site-header{position:absolute;top:0;left:0;width:1200px;height:128px;background:#fff}
.brand{left:145px;top:48px;display:flex;align-items:center;gap:10px;font-weight:700;font-size:20px;color:var(--navy);letter-spacing:.5px}
.brand-mark{width:26px;height:26px;background:var(--navy)}
.phone{right:145px;top:30px;font-size:24px;font-weight:600;color:var(--teal);display:flex;align-items:center;gap:8px}
.nav{right:145px;top:90px;display:flex;gap:34px;font-size:13px;font-weight:500;color:#333;list-style:none}
.nav li:first-child{color:var(--blue)}
/* hero */
.hero{top:128px;left:0;width:1200px;height:584px;background:linear-gradient(100deg,#5a1e12 0%,#8c3a22 30%,#a2472a 55%,#6e2816 80%,#3b140c 100%)}
.hero-caption{left:207px;top:342px;width:786px;height:58px;background:linear-gradient(90deg,rgba(13,74,154,.9),rgba(25,163,127,.9));color:#fff;font-size:31px;font-weight:600;display:flex;align-items:center;justify-content:center}
.hero-arrow{top:349px;width:44px;height:44px;border-radius:50%;background:rgba(120,170,150,.85);display:flex;align-items:center;justify-content:center}
.chevron{left:0;width:1200px;height:96px}
/* welcome */
.welcome{top:780px;left:147px;width:906px;text-align:center}
h2{font-size:34px;font-weight:600;color:var(--navy)}
.welcome p{margin-top:18px;font-size:19px;line-height:32px}
.btn{display:inline-block;background:var(--grad);color:#fff;font-size:16px;font-weight:500;padding:0 16px;line-height:44px}
.welcome .btn{margin-top:24px;width:128px;padding:0}
/* services */
.services{top:1077px;left:0;width:1200px;height:583px;background:linear-gradient(90deg,#eef1f6 0%,#eef1f6 40%,#c8cfd6 70%,#b8a89a 100%)}
.services-text{left:145px;top:1058px}
.services-text h2{margin-top:80px}
.services-text p{margin-top:10px;width:400px;font-size:19px;line-height:32px}
.service-item{left:145px;display:flex;align-items:center;gap:16px;font-size:36px;color:var(--navy);font-weight:500}
.service-icon{width:120px;height:120px;border-radius:50%;background:linear-gradient(135deg,var(--blue),var(--teal));display:flex;align-items:center;justify-content:center}
/* testimonials */
.testimonials-title{top:1732px;left:0;width:1200px;text-align:center}
.card{top:1799px;width:297px;height:327px;background:var(--soft);text-align:center}
.card p{padding:36px 30px 0;font-size:16px;line-height:29px}
.quote{font-family:Georgia,serif;font-size:84px;font-weight:700;color:var(--teal);line-height:60px;margin-top:14px;height:50px}
.card-name{position:absolute;bottom:0;left:0;width:100%;height:49px;line-height:49px;background:var(--grad);color:#fff;font-size:16px;font-weight:600}
/* contact */
.contact{top:2207px;left:0;width:1200px;height:600px;background:linear-gradient(160deg,#e9ebee,#f4f5f7 50%,#e3e6ea)}
.contact-title{top:2268px;left:0;width:1200px;text-align:center}
.field{height:39px;background:#fff;border:1px solid #c9ccd2;font-size:11px;color:#555;padding:12px 15px}
.select-arrow{position:absolute;right:14px;top:16px;width:0;height:0;border-left:5px solid transparent;border-right:5px solid transparent;border-top:6px solid #333}
.submit{left:547px;top:2576px;width:104px;text-align:center;padding:0}
/* footer */
.footer{top:2794px;left:0;width:1200px;height:120px;background:var(--footer)}
.footer-links{left:145px;top:2818px;font-size:13px;color:#8ea2c4;word-spacing:2px}
.footer-links span{margin:0 9px}
.copy{left:145px;top:2850px;font-size:13px;color:#8ea2c4}
.social{top:2832px;width:24px;height:24px;border-radius:50%;background:#2c4d80}
</style>
</head>
<body>

<header class="site-header">
  <div class="abs brand"><span class="brand-mark"></span>TKV ESTATES LAW</div>
  <div class="abs phone">
    <svg width="20" height="20" viewBox="0 0 24 24"><path fill="#19a37f" d="M6.6 10.8a15.1 15.1 0 0 0 6.6 6.6l2.2-2.2c.3-.3.7-.4 1-.2 1.1.4 2.3.6 3.6.6.6 0 1 .4 1 1V20c0 .6-.4 1-1 1A17 17 0 0 1 3 4c0-.6.4-1 1-1h3.5c.6 0 1 .4 1 1 0 1.3.2 2.5.6 3.6.1.3 0 .7-.2 1z"/></svg>
    555.013.4820
  </div>
  <ul class="abs nav"><li>HOME</li><li>ABOUT US</li><li>SERVICES</li><li>TESTIMONIALS</li><li>CONTACT US</li></ul>
</header>

<section class="abs hero" role="img" aria-label="Photo of a shelf of red leather-bound law report volumes"></section>
<div class="abs hero-caption">High quality estates and real estate law services</div>
<div class="abs hero-arrow" style="left:55px"><svg width="14" height="14" viewBox="0 0 14 14"><path d="M9 2 4 7l5 5" stroke="#1b2a3a" stroke-width="2.4" fill="none"/></svg></div>
<div class="abs hero-arrow" style="left:1099px"><svg width="14" height="14" viewBox="0 0 14 14"><path d="m5 2 5 5-5 5" stroke="#1b2a3a" stroke-width="2.4" fill="none"/></svg></div>
<svg class="abs chevron" style="top:616px" viewBox="0 0 1200 96" preserveAspectRatio="none">
  <defs><linearGradient id="g1" x1="0" x2="1"><stop offset="0" stop-color="#0d4a9a"/><stop offset=".5" stop-color="#19a37f"/><stop offset="1" stop-color="#0d4a9a"/></linearGradient></defs>
  <polygon points="0,92 600,0 1200,92 1200,96 0,96" fill="url(#g1)"/>
  <polygon points="0,96 600,14 1200,96" fill="#fff"/>
</svg>

<section class="abs welcome">
  <h2>Welcome to TKV Estates Law</h2>
  <p>Thank you for visiting TKV Estates Law, where I endeavor to earn your trust and provide you with high quality estates and real estate law services. My goal is to make you feel comfortable as soon as you step foot in my office.</p>
  <span class="btn">READ MORE</span>
</section>

<section class="abs services" role="img" aria-label="Photo of a hand signing a document with a fountain pen, fading into a light background"></section>
<div class="abs services-text">
  <h2>Services</h2>
  <p>I use my accounting background to provide a high quality legal experience for my estates and real estate clients.</p>
</div>
<div class="abs service-item" style="top:1298px">
  <div class="service-icon"><svg width="50" height="60" viewBox="0 0 50 60" fill="none" stroke="#fff" stroke-width="2"><rect x="10" y="4" width="34" height="46"/><rect x="4" y="10" width="34" height="46"/><path d="M11 20h20M11 27h20M11 34h20M11 41h14"/></svg></div>
  Estates Law
</div>
<div class="abs service-item" style="top:1434px">
  <div class="service-icon"><svg width="60" height="56" viewBox="0 0 60 56" fill="none" stroke="#fff" stroke-width="2"><path d="M18 24 32 10l14 14M22 21v14h20V21M29 35v-8h6v8"/><path d="M4 40h12l10 4h12l10-6c3-2 6 1 3 4L38 52H4"/></svg></div>
  Real Estate Law
</div>
<svg class="abs chevron" style="top:1564px" viewBox="0 0 1200 96" preserveAspectRatio="none">
  <polygon points="0,92 600,0 1200,92 1200,96 0,96" fill="url(#g1)"/>
  <polygon points="0,96 600,14 1200,96" fill="#fff"/>
</svg>

<h2 class="abs testimonials-title">What our clients says about us</h2>
<svg class="abs" style="left:54px;top:1950px" width="20" height="28" viewBox="0 0 20 28"><path d="M15 3 5 14l10 11" stroke="#0b2558" stroke-width="3.5" fill="none"/></svg>
<svg class="abs" style="left:1124px;top:1950px" width="20" height="28" viewBox="0 0 20 28"><path d="m5 3 10 11L5 25" stroke="#0b2558" stroke-width="3.5" fill="none"/></svg>
<article class="abs card" style="left:144px"><p>Quisque aliquet est vestibulum pulvinar. Pellentesque convallis molestie enim sit amet efficitur. Etiam id imperdiet lectus. Cras sollicitudin cursus dui placerat tincidunt vulputate erat.</p><div class="quote">”</div><div class="card-name">Mark Dale, City</div></article>
<article class="abs card" style="left:451px"><p>Fusce vitae lectus sit amet mi pulvinar maximus. Aenean placerat, nibh vel accumsan aliquet, magna nibh accumsan nibh, ac tempus nunc ipsum ac tellus. Cras augue magna.</p><div class="quote">”</div><div class="card-name">Emily, City</div></article>
<article class="abs card" style="left:758px"><p>Vestibulum ante ipsum primis in faucibus orci luctus et ultrices posuere cubilia Vestibulum eget nisl metus. Phasellus nisl est, condimentum faucibus in, sollic itudin metus.</p><div class="quote">”</div><div class="card-name">Alex, City</div></article>

<section class="abs contact" role="img" aria-label="Photo of scattered printed paper documents"></section>
<h2 class="abs contact-title">Contact Us</h2>
<div class="abs field" style="left:232px;top:2327px;width:240px">Name</div>
<div class="abs field" style="left:481px;top:2327px;width:238px">Email</div>
<div class="abs field" style="left:728px;top:2327px;width:239px">Phone</div>
<div class="abs field" style="left:232px;top:2375px;width:240px">City</div>
<div class="abs field" style="left:481px;top:2375px;width:238px">Service for<span class="select-arrow"></span></div>
<div class="abs field" style="left:728px;top:2375px;width:239px">Title</div>
<div class="abs field" style="left:232px;top:2423px;width:735px;height:127px">Message</div>
<span class="abs btn submit">SUBMIT</span>
<svg class="abs chevron" style="top:2698px" viewBox="0 0 1200 96" preserveAspectRatio="none">
  <polygon points="0,92 600,0 1200,92 1200,96 0,96" fill="url(#g1)"/>
  <polygon points="0,96 600,14 1200,96" fill="#06122b"/>
</svg>

<footer class="abs footer"></footer>
<div class="abs footer-links">Home<span>|</span>About Us<span>|</span>Services<span>|</span>Testimonials<span>|</span>Contact Us</div>
<div class="abs copy">Copyright © 2020 &nbsp; TKV Law. &nbsp;All rights reserved.</div>
<div class="abs social" style="left:971px" aria-label="Social link"></div>
<div class="abs social" style="left:1030px" aria-label="Social link"></div>

</body>
</html>
```